Book cover for LM

Design cover for a book of gratitude and inspiration.
Book trim size will be 6.5 x 6.5 inches, or 8 x 8 inches, hardcover, 96 pages
Title: Lantern Meadows
Subtitle: A Book of Gratitude and Inspiration
Author: Gus Halverd

```html
<!DOCTYPE html>
<html lang="en">
<head>
<meta charset="utf-8">
<title>Lantern Meadows — Cover Wrap</title>
<link rel="stylesheet" href="https://fonts.googleapis.com/css2?family=Cinzel:wght@400;600;700&family=Montserrat:wght@400;600&display=swap">
<style>
  :root {
    --page-bg: #ececec;
    --teal: #a3dbcf;
    --teal-deep: #8fcfc1;
    --ink: #2c2c2c;
    --band: #2f2f2f;
    --white: #ffffff;
    --accent: #e8a27f;
    --photo-slot: #e8e8e8;
    --text-muted: #3a3a3a;
  }
  * { box-sizing: border-box; margin: 0; padding: 0; }
  html, body { width: 1200px; height: 1200px; overflow: hidden; }
  body { background: var(--page-bg); position: relative; font-family: "Montserrat", sans-serif; }

  .cover-wrap {
    position: absolute; left: 67px; top: 343px;
    width: 1066px; height: 516px;
    background: var(--teal);
  }

  .back-cover { position: absolute; left: 0; top: 0; width: 518px; height: 466px; }
  .spine { position: absolute; left: 518px; top: 0; width: 32px; height: 516px; background: var(--band); }
  .front-cover { position: absolute; left: 550px; top: 0; width: 516px; height: 466px; overflow: hidden; }
  .bottom-band { position: absolute; left: 0; top: 466px; width: 1066px; height: 50px; background: var(--band); }

  .subtitle {
    font-family: "Cinzel", serif; color: var(--ink);
    text-align: center; font-weight: 600; letter-spacing: 0.02em; white-space: nowrap;
  }
  .title {
    font-family: "Cinzel", serif; color: var(--ink);
    text-align: center; font-weight: 400; line-height: 0.9; white-space: nowrap;
  }

  .back-cover .subtitle { position: absolute; left: 0; width: 518px; top: 43px; font-size: 15px; }
  .back-cover .title { position: absolute; left: 0; width: 518px; top: 60px; }
  .back-cover .title-line-1 { font-size: 46px; display: block; }
  .back-cover .title-line-2 { font-size: 54px; display: block; }

  .blurb {
    position: absolute; left: 62px; top: 159px; width: 394px;
    font-size: 7.2px; line-height: 13px; color: var(--text-muted); text-align: justify;
  }
  .blurb p + p { margin-top: 6px; }

  .divider { position: absolute; left: 62px; top: 361px; width: 392px; height: 2px; background: var(--accent); }

  .author-photo { position: absolute; left: 60px; top: 370px; width: 56px; height: 63px; background: var(--photo-slot); }
  .about-author {
    position: absolute; left: 122px; top: 366px; width: 328px;
    font-size: 7.2px; line-height: 11px; color: var(--text-muted); text-align: justify;
  }
  .about-author strong { font-weight: 600; }

  .spine-text {
    position: absolute; left: 0; top: 40px; width: 32px;
    writing-mode: vertical-rl; font-family: "Cinzel", serif; color: var(--white);
    display: flex; align-items: center; gap: 20px; white-space: nowrap;
  }
  .spine-title { font-size: 23px; line-height: 32px; }
  .spine-author { font-size: 17px; line-height: 32px; }

  .cover-art {
    position: absolute; left: 81px; top: 167px; width: 405px; height: 299px;
    background: radial-gradient(ellipse at 50% 45%, #f3e9e3 0%, #e9c8b3 35%, #d9b39c 55%, var(--teal-deep) 80%, var(--teal) 100%);
  }

  .front-cover .subtitle { position: absolute; left: 0; width: 516px; top: 30px; font-size: 19px; z-index: 2; }
  .front-cover .title { position: absolute; left: 0; width: 516px; top: 54px; z-index: 2; }
  .front-cover .title-line-1 { font-size: 68px; display: block; }
  .front-cover .title-line-2 { font-size: 86px; display: block; }

  .front-author {
    position: absolute; left: 550px; top: 466px; width: 516px; height: 50px;
    font-family: "Cinzel", serif; font-weight: 600; font-size: 29px; color: var(--white);
    display: flex; align-items: center; justify-content: center; letter-spacing: 0.02em;
  }
</style>
</head>
<body>
  <div class="cover-wrap">
    <section class="back-cover">
      <h2 class="subtitle">A Book of Gratitude and Inspiration</h2>
      <h1 class="title"><span class="title-line-1">LANTERN</span><span class="title-line-2">MEADOWS</span></h1>
      <div class="blurb">
        <p>Every morning offers a small reason to be thankful, and this book gathers them one page at a time. Short sayings sit beside quiet reflections, each one chosen to slow the reader down and bring attention back to what already feels good. Some pages invite a pause, others a deep breath, and a few ask for a pen so that a thought can be written down before it fades. The pieces can be read in order or opened at random, whenever a lift is needed during a long or busy day.</p>
        <p>Gratitude grows like a field of wildflowers: it spreads quietly, then suddenly fills the view. These pages follow that idea through the seasons, from early spring hope to the calm of a winter evening. Each saying is paired with a gentle question to carry into the day ahead. Readers will find words to share with friends, notes to keep by the bed, and reminders that kindness and wonder are always close at hand. It is a book to keep, to give, and to return to often for a simple daily lift.</p>
      </div>
      <div class="divider"></div>
      <div class="author-photo" role="img" aria-label="Author portrait"></div>
      <p class="about-author"><strong>About the Author:</strong> Gus Halverd writes short reflections on thankfulness and everyday hope. He has spent many years collecting sayings from friends, neighbours and travels, and he shares them in talks and small workshops. He lives near the coast with his family and a very patient garden.</p>
    </section>

    <div class="spine">
      <div class="spine-text">
        <span class="spine-title">LANTERN MEADOWS</span>
        <span class="spine-author">GUS HALVERD</span>
      </div>
    </div>

    <section class="front-cover">
      <div class="cover-art" role="img" aria-label="Two cupped hands holding a paper head silhouette filled with a brain made of flowers"></div>
      <h2 class="subtitle">A Book of Gratitude and Inspiration</h2>
      <h1 class="title"><span class="title-line-1">LANTERN</span><span class="title-line-2">MEADOWS</span></h1>
    </section>

    <div class="bottom-band"></div>
    <div class="front-author">GUS HALVERD</div>
  </div>
</body>
</html>
```